Tattoo Shop Business Card

I need a Business Card for the The Harbor Quill.

I'm thinking i want a double sided business card, really clean, very classy, one side the logo, and on the other my information. I'm pretty much open to anything, as long as its fun and captures class and elegance, while at the same time is edgy and tattooish.
I don't want your typical classic card. Add your own twist on it

Logo is attached to this brief

Please include:
Name
Position
Phone Number
Email
Website

Target Market(s)

I'm looking to capture potential clients for my tattoo shop so the card needs to be something they can fit in their wallet but they will also remember me when they see that card in there. My target audience is everyone over 18 that is intrigued by tattoos and piercings.

Industry/Entity Type

Business

Font styles to use
Serif

Colors

Designer to choose colors to be used in the design.

Requirements
Must have
• must be bold and something people will never forget

```html
<!DOCTYPE html>
<html lang="en">
<head>
<meta charset="utf-8">
<title>The Harbor Quill — Business Card</title>
<link rel="stylesheet" href="https://fonts.googleapis.com/css2?family=Montserrat:ital,wght@0,400;0,600;0,700;0,800;1,400&display=swap">
<style>
  :root {
    --page: #ffffff;
    --card: #e8ebed;
    --ink: #1d1d1f;
    --rule: #3a3a3c;
    --paper-text: #ffffff;
  }
  * { box-sizing: border-box; margin: 0; padding: 0; }
  html, body {
    width: 851px; height: 1200px; overflow: hidden;
    background: var(--page);
    font-family: "Montserrat", sans-serif;
    color: var(--ink);
  }
  .card {
    position: absolute;
    left: 61px; width: 728px;
    background: var(--card);
    box-shadow: 0 2px 6px rgba(0,0,0,0.18);
  }
  .card::before {
    content: ""; position: absolute; inset: 16px;
    border: 2px dotted var(--rule);
    pointer-events: none;
  }
  .card--front { top: 158px; height: 386px; }
  .card--back { top: 614px; height: 402px; }

  /* Front */
  .brand {
    position: absolute; top: 70px; left: 0; right: 0;
    display: flex; align-items: center; justify-content: center; gap: 20px;
  }
  .brand__dot {
    width: 26px; height: 26px; border-radius: 50%; background: var(--ink);
  }
  .brand__name {
    font-weight: 800; font-size: 62px; letter-spacing: 2px;
    text-transform: uppercase; color: var(--ink);
  }
  .front-details {
    position: absolute; top: 250px; left: 0; right: 0;
    text-align: center; font-weight: 600; font-size: 21px; line-height: 1.35;
  }
  .front-details strong { font-weight: 800; }

  /* Back */
  .divider {
    position: absolute; left: 356px; top: 16px; bottom: 16px;
    border-left: 2px dotted var(--rule);
  }
  .banner {
    position: absolute; top: 36px; height: 30px;
    background: var(--ink); color: var(--paper-text);
    font-weight: 700; font-size: 14px; letter-spacing: 5px;
    text-transform: uppercase;
    display: flex; align-items: center; justify-content: center;
    clip-path: polygon(10px 0, calc(100% - 10px) 0, 100% 50%, calc(100% - 10px) 100%, 10px 100%, 0 50%);
  }
  .banner--contact { left: 50px; width: 282px; }
  .banner--appointments { left: 386px; width: 290px; }

  .contact {
    position: absolute; left: 50px; top: 126px;
    font-size: 16px; line-height: 1.3;
  }
  .contact__name { font-weight: 800; font-size: 25px; letter-spacing: 0.5px; }
  .contact__role { font-style: italic; }
  .contact__block { margin-top: 26px; font-weight: 600; }
  .contact__block em { font-weight: 400; font-size: 13px; }
  .contact__web { font-weight: 800; }

  .appt {
    position: absolute; left: 400px; width: 250px;
    border-collapse: collapse;
    font-size: 12px; font-weight: 600;
  }
  .appt td { border: 2px solid var(--ink); height: 46px; }
  .appt .appt__label { width: 62px; text-align: center; }
  .appt--first { top: 130px; }
  .appt--second { top: 250px; }
</style>
</head>
<body>
  <section class="card card--front">
    <div class="brand">
      <span class="brand__dot"></span>
      <span class="brand__name">The Harbor Quill</span>
    </div>
    <div class="front-details">
      <p>John Doe | Tattoo Artist</p>
      <p>Address Line 1. Address Line 2.</p>
      <p>(000) 000 0000 | <strong>www.theharborquill.com</strong></p>
    </div>
  </section>

  <section class="card card--back">
    <div class="divider"></div>
    <div class="banner banner--contact">Contact Info</div>
    <div class="banner banner--appointments">Appointments</div>

    <div class="contact">
      <p class="contact__name">JOHN DOE</p>
      <p class="contact__role">Tattoo Artist</p>
      <p>john.doe@theharborquill.com</p>
      <div class="contact__block">
        <p>Address Line 1</p>
        <p>Address Line 2.</p>
        <p>(000) 000 0000 <em>(main)</em></p>
        <p>(000) 000 0000 <em>(cell)</em></p>
        <p class="contact__web">www.theharborquill.com</p>
      </div>
    </div>

    <table class="appt appt--first">
      <tr><td class="appt__label">Date</td><td></td></tr>
      <tr><td class="appt__label">Time</td><td></td></tr>
    </table>
    <table class="appt appt--second">
      <tr><td class="appt__label">Date</td><td></td></tr>
      <tr><td class="appt__label">Time</td><td></td></tr>
    </table>
  </section>
</body>
</html>
```